Web Design Project for Industrial Hemp

I'm launching a new company to grow Industrial Hemp and then to set up a manufacturing facility to process the crop each and every year. We require a complete end to end brand and livery suite and we will start with a web presence. We want to appeal to (a) Investors, Employees, Farmers, and consumers so as to engage with all our stakeholders. We want to create a whole new industry that becomes a game changer for environmentally friendly crop production. Hemp is gaining in popularity and credibility across the world!

Target Market(s)

Farmers to produce, Manufacturers who will purchase the raw materials, Investors who will invest in the project, Consumers who will buy Hemp Products

Industry/Entity Type

Industry

Requirements
Must have
• Environmentally Friendly
Carbon Neutral/Positive
Game Changer
Multi-Use Crop
50,000 products can be made from Hemp
Should not have
• Should avoid its relationship with cannabis but not ignore it! When the regulatory bodies acknowledge the benefits of cannabanoids, they will start to legalise the production of cannabis for sale on prescription

```html
<!DOCTYPE html>
<html lang="en">
<head>
<meta charset="utf-8">
<title>Greenfield Fibre Co</title>
<link rel="stylesheet" href="https://fonts.googleapis.com/css2?family=Archivo+Black&family=Arimo:wght@400;700&family=Roboto+Condensed:wght@400;700&family=PT+Sans&display=swap">
<style>
:root{
  --leaf:#6aa313;
  --leaf-dark:#4f8a0c;
  --lime:#9fd11a;
  --lime-text:#3d6b08;
  --grass:#5c8c10;
  --grass-dark:#4a760c;
  --ink:#222;
  --muted:#8a8a8a;
  --nav:#6c6c6c;
  --paper:#fff;
  --sky-top:#9fb6cc;
  --sky-mid:#5f7fa0;
  --lake:#274a7a;
}
*{box-sizing:border-box;margin:0;padding:0}
html,body{width:1200px;height:1200px;overflow:hidden}
body{position:relative;font-family:"Arimo",Arial,sans-serif;color:var(--ink);background:var(--grass)}
.abs{position:absolute}
.backdrop{left:0;top:0;width:1200px;height:900px;background:linear-gradient(180deg,var(--sky-top) 0%,#c9d5e2 18%,#8fa3bc 32%,#4d6d58 48%,#3e6a3a 60%,var(--lake) 70%,#2f5587 100%)}
.ground{left:0;top:900px;width:1200px;height:300px;background:var(--grass)}
.footer{left:0;top:1164px;width:1200px;height:36px;background:repeating-linear-gradient(180deg,var(--grass-dark) 0 2px,#527f0e 2px 4px)}
.footer p{position:absolute;left:201px;top:13px;font-size:9.5px;color:#fff}
.shell{left:192px;top:16px;width:816px;height:1128px;border-radius:10px;background:rgba(235,240,230,.55)}
.page{left:200px;top:24px;width:800px;height:1110px;border-radius:8px;background:var(--paper);overflow:hidden}
.header{left:0;top:0;width:800px;height:84px;background:linear-gradient(180deg,#f4f4f4,#e6e6e6)}
.brand{left:12px;top:38px;display:flex;align-items:center;gap:8px;font-weight:700;font-size:19px;color:var(--leaf-dark)}
.brand i{display:block;width:14px;height:14px;border-radius:50%;background:var(--leaf)}
.account{left:612px;top:17px;font-family:"Roboto Condensed",sans-serif;font-size:12.5px;color:var(--leaf);display:flex;gap:16px}
.social{left:718px;top:13px;display:flex;gap:5px}
.social span{width:22px;height:22px;border-radius:50%;background:var(--leaf)}
.nav{left:274px;top:54px;display:flex;font-family:"Roboto Condensed",sans-serif;font-size:12.5px;color:var(--nav)}
.nav a{color:inherit;text-decoration:none;padding:0 9px;border-left:1px dotted #bbb}
.nav a:first-child{border:0;padding-left:0;color:var(--leaf)}
.search{left:610px;top:50px;width:180px;height:19px;border:1px solid var(--leaf);background:#fff}
.search svg{position:absolute;right:3px;top:2px}
.rule{left:0;top:84px;width:800px;height:5px;background:var(--leaf)}
.hero{left:0;top:89px;width:800px;height:341px;background:radial-gradient(ellipse at 65% 55%,#8bd12a 0%,#4c9a10 35%,#1a4a08 65%,#0b200a 100%)}
.hero h1{position:absolute;left:9px;top:22px;font-family:"Archivo Black",sans-serif;font-size:27px;color:#fff;font-weight:400;letter-spacing:.5px}
.hero h2{position:absolute;left:9px;top:55px;font-family:"Roboto Condensed",sans-serif;font-weight:400;font-size:16px;color:#fff}
.card{top:446px;width:256px;height:218px}
.card .photo{position:absolute;left:0;top:0;width:100%;height:122px}
.card h3{position:absolute;left:0;top:98px;width:100%;height:24px;background:rgba(255,255,255,.55);text-align:center;font-family:"Roboto Condensed",sans-serif;font-weight:700;font-size:16px;line-height:24px;color:#1e1e1e}
.card .body{position:absolute;left:0;top:124px;width:100%;height:94px;background:var(--lime);border-radius:0 0 3px 3px;padding:9px 14px 0;font-size:10.6px;line-height:13.4px;color:#fff}
.card .more{position:absolute;right:8px;bottom:4px;font-weight:700;font-size:11px;color:var(--lime-text)}
.divider{left:140px;width:520px;height:1px;background:linear-gradient(90deg,transparent,#ddd,transparent)}
.about-tag{left:0;top:710px}
.about-text{left:208px;top:700px;width:510px;font-size:11.6px;line-height:14.4px;color:var(--muted)}
.about-text b{display:block;margin-top:5px;color:var(--leaf-dark);font-size:11.5px}
.col-title{font-family:"PT Sans",sans-serif;font-size:15px;color:var(--leaf);letter-spacing:-.2px}
.news{left:20px;width:270px}
.date{position:absolute;left:0;top:0;width:34px;height:34px;background:var(--leaf);color:#fff;text-align:center;font-size:11px;line-height:12px;padding-top:4px}
.date b{display:block;font-weight:400;font-size:12px}
.news h4{position:absolute;left:41px;top:0;font-weight:400;font-size:10px;color:var(--leaf)}
.news p{position:absolute;left:41px;top:14px;width:232px;font-size:8.4px;line-height:10.6px;color:#444}
.dots{left:18px;width:228px;border-top:1px dotted #aaa}
.vline{top:860px;width:1px;height:200px;background:#e4e4e4}
.likes{left:324px;top:888px;display:grid;grid-template-columns:repeat(4,37px);grid-gap:1px}
.likes span{height:37px}
.like-btn{left:444px;top:858px;width:37px;height:17px;border:1px solid #bbb;background:#eee;font-size:8px;line-height:15px;text-align:center;color:#333}
.likes-text{left:325px;top:974px;width:160px;font-size:8.8px;line-height:11px;color:var(--muted)}
.testi{left:504px;width:260px}
.testi .ph{position:absolute;left:0;top:0;width:58px;height:58px;border-radius:8px;background:linear-gradient(135deg,#c89a70,#6c4a30)}
.testi p{position:absolute;left:65px;top:0;width:190px;font-size:8.8px;line-height:11.4px;color:var(--muted)}
.testi .meta{position:absolute;left:65px;top:42px;font-size:9px;font-weight:700;color:var(--lime);line-height:13.5px}
.testi .meta b{display:block;color:var(--leaf-dark)}
</style>
</head>
<body>
<div class="abs backdrop" role="img" aria-label="Mountain lake landscape with snowy peaks and green hills"></div>
<div class="abs ground"></div>
<div class="abs footer"><p>© 2013 Greenfield Fibre Co. All rights reserved</p></div>

<div class="abs shell"></div>
<main class="abs page">
  <header class="abs header">
    <div class="abs brand"><i></i>Greenfield Fibre Co</div>
    <div class="abs account"><span>LOG IN</span><span>SIGN UP</span></div>
    <div class="abs social"><span></span><span></span><span></span></div>
    <nav class="abs nav"><a href="#">HOME</a><a href="#">ABOUT US</a><a href="#">FORMS</a><a href="#">PRODUCTS</a><a href="#">CONTACT US</a></nav>
    <div class="abs search"><svg width="12" height="12" viewBox="0 0 12 12"><circle cx="5" cy="5" r="3.6" fill="none" stroke="#6aa313" stroke-width="1.5"/><line x1="7.6" y1="7.6" x2="11" y2="11" stroke="#6aa313" stroke-width="1.8"/></svg></div>
  </header>
  <div class="abs rule"></div>
  <section class="abs hero" role="img" aria-label="Close-up of bright green hemp leaves">
    <h1>LOREM IPSUM DOLOR SIT AMET</h1>
    <h2>LOREM IPSUM DOLOR SIT AMET</h2>
  </section>

  <article class="abs card" style="left:0">
    <div class="photo" role="img" aria-label="Group of smiling employees" style="background:linear-gradient(135deg,#f2f2f2,#c9c9c9 50%,#3a3a3a)"></div>
    <h3>EMPLOYEES</h3>
    <div class="body">Lorem ipsum dolor sit amet, consectetuer adipiscing elit, sed diam nonummy nibh euismod tincidunt ut laoreet dolore magna aliquam erat volutpat. Ut wisi enim ad minim veniam, quis nostrud exerci tation<span class="more">READMORE...</span></div>
  </article>
  <article class="abs card" style="left:272px">
    <div class="photo" role="img" aria-label="Businessman in an office" style="background:linear-gradient(90deg,#5c7ea0,#b8c6d6 45%,#2a2f3a 60%,#c0c8d2)"></div>
    <h3>INVESTORS</h3>
    <div class="body">Lorem ipsum dolor sit amet, consectetuer adipiscing elit, sed diam nonummy nibh euismod tincidunt ut laoreet dolore magna aliquam erat volutpat. Ut wisi enim ad minim veniam, quis nostrud exerci tation<span class="more">READMORE...</span></div>
  </article>
  <article class="abs card" style="left:544px">
    <div class="photo" role="img" aria-label="Shoppers carrying colourful bags" style="background:linear-gradient(120deg,#8a7058,#6d8cb0 40%,#d04a5a 65%,#e8d0b0)"></div>
    <h3>CONSUMERS</h3>
    <div class="body">Lorem ipsum dolor sit amet, consectetuer adipiscing elit, sed diam nonummy nibh euismod tincidunt ut laoreet dolore magna aliquam erat volutpat. Ut wisi enim ad minim veniam, quis nostrud exerci tation<span class="more">READMORE...</span></div>
  </article>

  <div class="abs divider" style="top:683px"></div>
  <svg class="abs about-tag" width="190" height="46" viewBox="0 0 190 46">
    <defs><linearGradient id="tagFill" x1="0" y1="0" x2="0" y2="1"><stop offset="0" stop-color="#a2cf2c"/><stop offset="1" stop-color="#5e9410"/></linearGradient></defs>
    <polygon points="0,0 168,0 188,23 168,46 0,46" fill="url(#tagFill)"/>
    <text x="22" y="31" font-family="Archivo Black, sans-serif" font-size="19" fill="#fff">ABOUT US</text>
  </svg>
  <div class="abs about-text">Lorem ipsum dolor sit amet, consectetuer adipiscing elit, sed diam nonummy nibh euismod tincidunt ut laoreet dolore magna aliquam erat volutpat. Ut wisi enim ad minim veniam, quis nostrud exerci tation ullamcorper suscipit lobortis nisl ut aliquip ex ea commodo consequat. Duis autem vel eum iriure dolor in hendrerit in vulputate velit esse molestie consequa.<b>READMORE...</b></div>
  <div class="abs divider" style="top:778px"></div>

  <h5 class="abs col-title" style="left:20px;top:835px">LATEST NEWS</h5>
  <div class="abs news" style="top:866px"><div class="date"><b>04</b>APR</div><h4>Lorem ipsum dolor sit amet</h4><p>sed diam nonummy nibh euismod tincidunt ut laoreet dolore magna aliquam erat..</p></div>
  <div class="abs dots" style="top:914px"></div>
  <div class="abs news" style="top:926px"><div class="date"><b>04</b>APR</div><h4>Lorem ipsum dolor sit amet</h4><p>sed diam nonummy nibh euismod tincidunt ut laoreet dolore magna aliquam erat..</p></div>
  <div class="abs dots" style="top:975px"></div>
  <div class="abs news" style="top:987px"><div class="date"><b>04</b>APR</div><h4>Lorem ipsum dolor sit amet</h4><p>sed diam nonummy nibh euismod tincidunt ut laoreet dolore magna aliquam erat..</p></div>

  <div class="abs vline" style="left:314px"></div>
  <h5 class="abs col-title" style="left:324px;top:835px">FRIENDLINK LIKES</h5>
  <div class="abs like-btn">Like</div>
  <div class="abs likes" role="img" aria-label="Grid of follower profile photos">
    <span style="background:#5a4a48"></span><span style="background:#c8b49a"></span><span style="background:#8aa8d0"></span><span style="background:#b88a70"></span>
    <span style="background:#7a90a8"></span><span style="background:#c09a88"></span><span style="background:#a88468"></span><span style="background:#b8b0a8"></span>
  </div>
  <p class="abs likes-text">Lorem ipsum dolor sit amet, consectetuer adipiscing elit, sed diam nonummy nibh euismod</p>
  <div class="abs vline" style="left:486px"></div>

  <h5 class="abs col-title" style="left:509px;top:835px">TESTIMONIALS</h5>
  <div class="abs testi" style="top:868px"><div class="ph" role="img" aria-label="Customer at her desk"></div><p>Lorem ipsum dolor sit amet, consectetuer adipiscing elit, sed diam nonummy nibh euismod tincidunt ut laoreet</p><div class="meta">02-06-2013 ON SUNDAY<b>READMORE</b></div></div>
  <div class="abs dots" style="left:502px;top:950px;width:228px"></div>
  <div class="abs testi" style="top:968px"><div class="ph" role="img" aria-label="Customer at her desk"></div><p>Lorem ipsum dolor sit amet, consectetuer adipiscing elit, sed diam nonummy nibh euismod tincidunt ut laoreet</p><div class="meta">02-06-2013 ON SUNDAY<b>READMORE</b></div></div>
</main>
</body>
</html>
```